Purchasing community for life science startups needs landing page for collecting of contact adresses

We are the "Pipette Union", the first purchasing community for life science startups. The idea is to bundle the needs of several smaller companies (laboratories) and to buy lab consumables and chemicals in larger quantities. This bargaining position, at the end of all participants can buy their products very low prices. In the attached powerpoint file you will find an idea and some elements, which demonstrate a little the style, which came into my mind.
Urlaub/Ferien
Target Market(s)
Our target customers are startups and smaller biotech companies, which are too small to get the best prices. The aim of this landing page is to collect all interested parties.
Look and feel

```html
<!DOCTYPE html>
<html lang="en">
<head>
<meta charset="utf-8">
<title>Pipette Union – Einkaufsgemeinschaft LifeScience</title>
<link rel="stylesheet" href="https://fonts.googleapis.com/css2?family=Open+Sans:wght@300;400;600;700;800&display=swap">
<style>
:root{
  --sky:#bfe7fb;
  --sky-deep:#8fd4f7;
  --navy:#0b3a8c;
  --band:#0a5aa8;
  --band-dark:#083f8a;
  --field-line:#5aa8ee;
  --magenta:#b0128f;
  --violet:#7a2fd0;
  --pale:#d6f0fc;
  --ink:#222b36;
  --footer:#061a33;
  --link-cyan:#64d2ff;
}
*{box-sizing:border-box;margin:0;padding:0}
html,body{width:1200px;height:1200px;overflow:hidden}
body{font-family:"Open Sans",sans-serif;color:var(--ink);position:relative;background:var(--pale)}
.abs{position:absolute}

.hero{left:0;top:0;width:1200px;height:432px;background:linear-gradient(180deg,var(--sky-deep) 0%,var(--sky) 60%,#cdeefc 100%);overflow:hidden}
.blob{position:absolute;border-radius:50%;background:rgba(120,225,255,.45)}

.brand-mark{left:208px;top:45px;width:62px;height:62px;background:var(--navy)}
.brand-name{left:281px;top:48px;font-size:27px;font-weight:700;color:#0d2240;letter-spacing:-.3px}
.brand-sub{left:281px;top:82px;font-size:15px;font-weight:400;color:#0d2240}

.save{left:210px;top:150px;font-size:50px;font-weight:800;color:var(--navy);line-height:1}
.upto{left:211px;top:206px;font-size:24px;font-weight:700;color:#0d2240}
.on{left:213px;top:255px;font-size:24px;font-weight:700;color:#0d2240}
.pct{left:282px;top:192px;font-size:86px;font-weight:800;color:var(--magenta);letter-spacing:-2px;line-height:1}
.purchases{left:209px;top:278px;font-size:52px;font-weight:800;color:var(--navy);line-height:1}
.tagline{left:212px;top:350px;width:286px;border-top:1px solid #1d2f55;border-bottom:1px solid #1d2f55;padding:4px 0 2px 1px;font-size:14px;color:#0d2240;display:flex;justify-content:space-between;align-items:center}
.tagline svg{margin-right:10px}

.hex{left:488px;top:148px}
.hex-text{left:490px;top:172px;width:176px;text-align:center}
.hex-text .buy{font-size:22px;font-weight:600;color:var(--magenta);line-height:1.2}
.hex-text p{font-size:14px;color:#2a3a4e;line-height:1.4}

.lab-art{left:620px;top:100px;width:390px;height:348px;border-radius:40px 40px 12px 12px;background:linear-gradient(90deg,rgba(120,120,130,.55) 0%,rgba(150,150,160,.45) 45%,rgba(200,120,200,.4) 75%,rgba(140,90,200,.4) 100%)}

.signup{left:0;top:432px;width:1200px;height:344px;background:var(--band);overflow:hidden}
.signup .wave{position:absolute;left:120px;top:90px;width:420px;height:300px;border-radius:45% 55% 40% 60%;background:rgba(20,110,210,.55)}
.field{left:214px;width:293px;height:40px;border:2px solid var(--field-line);background:var(--band-dark);color:#9fc2ea;font-size:13px;padding:0 14px;line-height:36px}
.cta{left:214px;top:674px;width:293px;height:44px;border:2px solid #e8f4ff;background:linear-gradient(180deg,#2c8bf0,#0b55cf);color:#fff;font-size:14px;font-weight:700;text-align:center;line-height:40px;letter-spacing:.2px}
.ask-title{left:550px;top:502px;font-size:24px;font-weight:700;color:#fff}
.ask-lead{left:548px;top:540px;font-size:14px;color:#fff}
.ask-lead b{color:var(--link-cyan);font-weight:700}
.ask-note{left:550px;top:578px;width:360px;font-size:12.5px;color:#fff;line-height:1.45}
.checks{left:552px;top:638px;list-style:none}
.checks li{display:flex;align-items:center;height:30px;font-size:18px;font-weight:300;color:#fff}
.checks svg{margin-right:20px}

.about{left:0;top:776px;width:1200px;height:334px;background:var(--pale);overflow:hidden}
.about .glow{position:absolute;left:775px;top:90px;width:520px;height:420px;border-radius:50%;background:rgba(240,252,255,.7)}
.about h2{position:absolute;left:216px;font-size:19px;font-weight:600}
.about p{position:absolute;left:216px;width:790px;font-size:12.8px;line-height:1.45;color:var(--ink)}
.goal{color:var(--violet)}
.principle{color:#1456c4}
.simple{color:var(--magenta)}

.footer{left:0;top:1110px;width:1200px;height:90px;background:var(--footer);text-align:center;color:#c7d2e0}
.footer .links{margin-top:24px;font-size:13px}
.footer .copy{margin-top:8px;font-size:11px;color:#9fb0c4}
</style>
</head>
<body>

<section class="abs hero">
  <div class="blob" style="left:-60px;top:40px;width:190px;height:230px"></div>
  <div class="blob" style="left:1040px;top:90px;width:260px;height:230px"></div>
  <div class="blob" style="left:880px;top:-60px;width:240px;height:150px"></div>
</section>

<div class="abs brand-mark" aria-hidden="true"></div>
<div class="abs brand-name">PIPETTE UNION</div>
<div class="abs brand-sub">Einkaufsgemeinschaft LifeScience</div>

<div class="abs save">SAVE</div>
<div class="abs upto">UP TO</div>
<div class="abs pct">40%</div>
<div class="abs on">ON</div>
<div class="abs purchases">PURCHASES</div>
<div class="abs tagline"><span>JOINT PURCHASE AT &nbsp;WHOLESALE PRICES</span>
  <svg width="8" height="10" viewBox="0 0 8 10"><path d="M0 0L8 5L0 10Z" fill="#b0128f"/></svg></div>

<svg class="abs hex" width="180" height="156" viewBox="0 0 180 156">
  <defs><linearGradient id="hexFill" x1="0" y1="0" x2="0" y2="1"><stop offset="0" stop-color="#e2f6ff"/><stop offset="1" stop-color="#bfe6fa"/></linearGradient></defs>
  <polygon points="45,2 135,2 178,78 135,154 45,154 2,78" fill="url(#hexFill)" stroke="#3a9ee6" stroke-width="1.5"/>
</svg>
<div class="abs hex-text">
  <div class="buy">Buy</div>
  <p>Lab Consumables<br>and Chemicals<br>in Larger Quantities</p>
</div>

<div class="abs lab-art" role="img" aria-label="Illustration of a laboratory microscope, a pipette dropper and a rack of four coloured test tubes"></div>

<section class="abs signup"><div class="wave"></div></section>

<div class="abs field" style="top:510px">Email Address</div>
<div class="abs field" style="top:561px">First Name</div>
<div class="abs field" style="top:611px">Last Name</div>
<div class="abs cta">PREISLISTE PER EMAIL ERHALTEN</div>

<h1 class="abs ask-title">Are you interested in participating?</h1>
<div class="abs ask-lead">Then please do not hesitate to <b>sign up</b> for our list of interested parties.</div>
<div class="abs ask-note">To get an impression of our prices, we send you a preliminary price list and ask for feedback.</div>
<ul class="abs checks">
  <li><svg width="18" height="14" viewBox="0 0 18 14"><path d="M1 7L6.5 12L17 1" fill="none" stroke="#fff" stroke-width="2"/></svg>Which articles interest you?</li>
  <li><svg width="18" height="14" viewBox="0 0 18 14"><path d="M1 7L6.5 12L17 1" fill="none" stroke="#fff" stroke-width="2"/></svg>In what quantities do you need these?</li>
  <li><svg width="18" height="14" viewBox="0 0 18 14"><path d="M1 7L6.5 12L17 1" fill="none" stroke="#fff" stroke-width="2"/></svg>Which are still missing?</li>
</ul>

<section class="abs about">
  <div class="glow"></div>
  <h2 class="goal" style="top:31px">Our Goal</h2>
  <p style="top:72px">Our goal is to build the first LifeScience Laboratory purchasing community, which allows each participant to cover their laboratory supplies at wholesale prices.</p>
  <h2 class="principle" style="top:128px">The Campaign Principle.</h2>
  <p style="top:167px">The campaign principle. We bundle your annual demand for chemicals, consumables and laboratory supplies and act as a strong negotiating partner for manufacturers and suppliers. The more participants participate, the bigger our bargaining power, the better our purchase prices.</p>
  <h2 class="simple" style="top:226px">Keep it Simple.</h2>
  <p style="top:266px">Keep it simple. We waive framework contracts, minimum order quantities and other obligations! If you like the negotiated price, then you normally order by order in the laboratory campaign your needs.</p>
</section>

<footer class="abs footer">
  <div class="links">IMPRINT &nbsp;|&nbsp; DATA PROTECTION</div>
  <div class="copy">© 2018 Pipette Union · All Rights Reserved.</div>
</footer>

</body>
</html>
```